Software product web site / landing page

We went to update our web site and landing pages

https://www.velmarin.com
https://www.tasknote7qx.com

with - mobile first design
- complementing our logo colors (blue/green)

The design should have a home/landing page and a detail page.

Style: minimalist/modern - abstract - friendly

Target Market(s)

Business with Professional Services department

Industry/Entity Type

Software

Number of Pages Required

2 page

Font styles to use
Sans Serif

Requirements
Must have
• easy to convert to html/scss for mobile + desktop
Nice to have
• apply this to web page:
• https://www.harborpatterncraft.com/guidelines/overview/
Should not have
• blogvane look

```html
<!DOCTYPE html>
<html lang="en">
<head>
<meta charset="utf-8">
<title>Velmarin – Time + Expense</title>
<link href="https://fonts.googleapis.com/css2?family=Poppins:wght@600;700&family=Lato:wght@400;700&display=swap" rel="stylesheet">
<style>
:root{
  --teal:#6bbfcf;
  --teal-light:#c6eff4;
  --ice:#eefafb;
  --blue:#2f6aa0;
  --navy:#24508a;
  --dark:#1e1e1e;
  --green:#7dc33b;
  --ink:#1a1a1a;
  --grey:#666;
  --card:#f2f2f2;
  --footer:#5ea4b4;
  --white:#fff;
}
*{box-sizing:border-box;margin:0;padding:0}
html,body{width:1200px;height:3169px;overflow:hidden}
body{font-family:"Lato",sans-serif;color:var(--ink);background:var(--white)}
section,header,footer{position:relative;width:1200px;overflow:hidden}
.abs{position:absolute}
.rule{position:absolute;left:160px;width:128px;height:2px;background:var(--white)}
.rule.dark{background:var(--ink)}
.headline{font-family:"Poppins",sans-serif;font-weight:700;font-size:44px;line-height:46px;letter-spacing:.5px}
.btn{position:absolute;display:flex;align-items:center;justify-content:center;background:var(--green);color:var(--white);font-weight:700;font-size:12px;letter-spacing:.5px;text-transform:uppercase}

/* header */
.site-header{height:61px;background:var(--white)}
.brand{position:absolute;left:160px;top:14px;display:flex;align-items:center;gap:8px;font-family:"Lato",sans-serif;font-weight:700;font-size:26px;color:var(--ink)}
.brand .dot{width:26px;height:26px;border-radius:50%;background:var(--blue)}
.nav{position:absolute;right:160px;top:22px;display:flex;gap:21px;font-size:13px;color:#333}
.nav a{color:inherit;text-decoration:none;position:relative}
.nav a.active::after{content:"";position:absolute;left:0;right:0;bottom:-23px;height:4px;background:var(--green)}

/* hero */
.hero{height:467px;background:var(--teal)}
.hero .band{position:absolute;left:0;right:0;top:383px;height:84px;background:var(--teal-light)}
.hero .rule{top:165px}
.hero-title{position:absolute;left:237px;top:192px;color:var(--white);font-family:"Poppins",sans-serif;font-weight:700;font-size:54px;line-height:48px;letter-spacing:1px}
.hero-sub{position:absolute;left:237px;top:323px;width:290px;color:var(--white);font-size:12px;line-height:16px;text-transform:uppercase}
.hero-art{position:absolute;left:560px;top:60px;width:570px;height:410px;background:linear-gradient(160deg,rgba(160,220,232,.7),rgba(47,90,160,.85));border-radius:4px}

/* features */
.features{height:499px;background:var(--ice)}
.feature{position:absolute;width:276px;text-align:center}
.feature .icon{width:60px;height:60px;border-radius:50%;background:var(--teal);margin:0 auto;display:flex;align-items:center;justify-content:center}
.feature.current .icon{background:var(--navy)}
.feature h3{margin-top:32px;font-size:14px;font-weight:700;letter-spacing:1px;color:var(--ink)}
.feature.current h3{color:var(--blue)}
.feature p{margin-top:20px;font-size:11px;line-height:15px;color:var(--grey);padding:0 12px}
.feature .line{position:absolute;left:0;right:0;top:189px;height:2px;background:var(--teal)}

/* management */
.management{height:467px;background:var(--blue);color:var(--white)}
.management .rule{top:59px}
.management .headline{position:absolute;left:237px;top:97px}
.management .copy{position:absolute;left:237px;top:261px;width:390px;font-size:11px;line-height:16px}
.video{position:absolute;left:725px;top:116px;width:315px;height:184px;border:5px solid var(--white);background:linear-gradient(180deg,#e6eef3,#b9c6d1)}
.video .play{position:absolute;left:130px;top:62px;width:50px;height:50px;border-radius:50%;background:rgba(255,255,255,.75)}
.caption{position:absolute;left:725px;top:315px;width:315px;font-size:11px;font-weight:700;line-height:16px;text-transform:uppercase}

/* partner */
.partner{height:528px;background:var(--dark);color:var(--white)}
.partner .rule{top:61px}
.partner .headline{position:absolute;left:237px;top:101px}
.partner .lead{position:absolute;left:237px;top:222px;width:360px;font-size:14px;line-height:18px;text-transform:uppercase}
.partner .note{position:absolute;left:237px;top:266px;font-size:11px;color:var(--green)}
.partner .copy{position:absolute;left:237px;top:290px;width:350px;font-size:11px;line-height:17px}
.checks{position:absolute;left:237px;top:378px;list-style:none}
.checks li{display:flex;align-items:center;gap:10px;font-size:17px;height:32px}
.badge{position:absolute;left:754px;top:74px;width:218px;height:52px;border-radius:6px;background:#2a2a2a;border:1px solid #3a3a3a}
.badge span{position:absolute;left:10px;top:8px;width:62px;height:36px;border-radius:18px;background:#2b9bd6}
.panel{position:absolute;left:663px;top:175px;width:377px;height:292px;background:var(--white);color:#333;font-size:7px}
.panel .bar{height:12px;background:#e4e8ec}
.panel h4{font-size:8px;padding:6px 8px 2px;font-weight:700}
.panel table{width:calc(100% - 16px);margin:0 8px;border-collapse:collapse}
.panel td,.panel th{text-align:left;padding:2px 3px;border-bottom:1px solid #eee;font-weight:400}
.panel th{color:#888}

/* demo */
.demo{height:393px;background:var(--ice)}
.demo .rule{top:59px}
.demo .headline{position:absolute;left:237px;top:91px;color:var(--ink);width:520px}
.demo .sub{position:absolute;left:237px;top:262px;font-size:11px;font-weight:700;text-transform:uppercase}
.portrait{position:absolute;left:760px;top:17px;width:280px;height:376px;background:linear-gradient(180deg,#d9e1e6,#4b5563)}

/* news */
.news{height:406px;background:var(--white)}
.news h2{position:absolute;top:50px;left:0;right:0;text-align:center;font-size:15px;font-weight:400;letter-spacing:1px}
.card{position:absolute;top:93px;width:430px;height:188px;background:var(--card)}
.date{position:absolute;left:30px;top:28px;width:46px;text-align:center;color:var(--white)}
.date .d{background:var(--blue);font-size:20px;font-weight:700;height:28px;line-height:28px}
.date .m{background:var(--green);font-size:11px;font-weight:700;height:21px;line-height:21px}
.card h3{position:absolute;left:102px;top:30px;font-size:19px;font-weight:700}
.card .meta{position:absolute;left:102px;top:58px;font-size:9px;color:#555;text-transform:uppercase;letter-spacing:.3px}
.card .excerpt{position:absolute;left:30px;top:98px;width:370px;font-size:11px;line-height:16px;color:#555}
.card .more{color:var(--ink);text-decoration:underline}

/* newsletter */
.newsletter{height:91px;background:var(--teal-light)}
.newsletter h2{position:absolute;left:160px;top:33px;font-size:20px;font-weight:400;color:var(--ink)}
.newsletter .field{position:absolute;left:537px;top:28px;width:383px;height:33px;background:var(--white);font-size:11px;color:#777;padding:10px 14px}
.newsletter .btn{left:920px;top:28px;width:120px;height:33px}

/* footer */
.site-footer{height:257px;background:var(--footer);color:var(--white)}
.site-footer .brand{top:40px;color:var(--white)}
.site-footer .brand .dot{background:var(--white)}
.about{position:absolute;left:160px;top:90px;width:200px;font-size:10px;line-height:13px}
.copyright{position:absolute;left:160px;top:193px;font-size:10px}
.fcol{position:absolute;top:52px}
.fcol h4{font-size:11px;font-weight:700;letter-spacing:.5px;margin-bottom:16px}
.fcol ul{list-style:none}
.fcol li{font-size:10px;height:22px;display:flex;align-items:flex-start;gap:10px}
.fcol li::before{content:"›"}
.contact li::before{content:none}
.contact li{gap:10px;height:26px;line-height:13px}
.social{display:flex;gap:16px;margin-top:10px}
.social span{width:14px;height:14px;border-radius:50%;background:var(--white)}
</style>
</head>
<body>

<header class="site-header">
  <div class="brand"><span class="dot"></span>Velmarin</div>
  <nav class="nav">
    <a class="active">HOME</a><a>FEATURES</a><a>PRODUCTS</a><a>SOLUTIONS</a><a>SUPPORT</a><a>BLOG</a>
  </nav>
</header>

<section class="hero">
  <div class="band"></div>
  <div class="rule"></div>
  <h1 class="hero-title">time +<br>expense</h1>
  <p class="hero-sub">Capture time and expenses in a weekly timesheet or individually in Cloudmerit or mobile.</p>
  <div class="hero-art" role="img" aria-label="Illustration of a figure dragging chained coins and a clock toward a large arrow"></div>
</section>

<section class="features">
  <div class="feature" style="left:160px;top:59px">
    <div class="icon"><svg width="26" height="26" viewBox="0 0 26 26" fill="none" stroke="#fff" stroke-width="2"><rect x="5" y="4" width="16" height="19" rx="2"/><line x1="9" y1="10" x2="17" y2="10"/><line x1="9" y1="14" x2="17" y2="14"/><line x1="9" y1="18" x2="14" y2="18"/></svg></div>
    <h3>PROJECTS</h3>
    <p>Assign Time to Projects. Projects can be created from Opportunities or from a Template.</p>
    <div class="line"></div>
  </div>
  <div class="feature current" style="left:462px;top:59px">
    <div class="icon"><svg width="28" height="28" viewBox="0 0 28 28" fill="none" stroke="#fff" stroke-width="2"><circle cx="14" cy="14" r="10"/><path d="M14 8v6l4 3"/></svg></div>
    <h3>TIME</h3>
    <p>Capture Time in a weekly Timesheet or individually via Mobile or directly in any Cloudmerit Object</p>
    <div class="line"></div>
  </div>
  <div class="feature" style="left:764px;top:59px">
    <div class="icon"><svg width="26" height="26" viewBox="0 0 26 26" fill="none" stroke="#fff" stroke-width="2"><circle cx="13" cy="13" r="9"/><path d="M16 9h-4a2 2 0 0 0 0 4h2a2 2 0 0 1 0 4h-4M13 7v12"/></svg></div>
    <h3>EXPENSES</h3>
    <p>Enter Expenses in a Table, Import from (Credit Card) Statements, Mobile with Receipt picture</p>
    <div class="line"></div>
  </div>
  <div class="feature" style="left:160px;top:317px">
    <div class="icon"><svg width="26" height="26" viewBox="0 0 26 26" fill="none" stroke="#fff" stroke-width="2"><circle cx="13" cy="13" r="4"/><circle cx="13" cy="13" r="9" stroke-dasharray="3 3"/></svg></div>
    <h3 style="margin-top:32px">RESOURCES</h3>
    <p>Manage Employees and Contractors</p>
  </div>
  <div class="feature" style="left:462px;top:317px">
    <div class="icon"><svg width="26" height="26" viewBox="0 0 26 26" fill="none" stroke="#fff" stroke-width="2"><rect x="6" y="4" width="14" height="19" rx="1"/><line x1="10" y1="10" x2="16" y2="10"/><line x1="10" y1="14" x2="16" y2="14"/></svg></div>
    <h3 style="margin-top:32px">BILLING</h3>
    <p>Create Customer Invoices based on Time + Material or fixed price.</p>
  </div>
  <div class="feature" style="left:764px;top:317px">
    <div class="icon"><svg width="26" height="26" viewBox="0 0 26 26" fill="none" stroke="#fff" stroke-width="2"><circle cx="12" cy="12" r="7"/><path d="M12 8v4h3M17 17l5 5"/></svg></div>
    <h3 style="margin-top:32px">TIME-OFF</h3>
    <p>Manage Entitlements, Time-off Requests as well as Holidays and Leave</p>
  </div>
</section>

<section class="management">
  <div class="rule"></div>
  <h2 class="headline">time and<br>expense<br>management</h2>
  <p class="copy">Velmarin is professional grade time and expense management software that gives you the power to seamlessly integrate project and resource management with billing – from opportunity to project to invoice and payroll integration. Streamline processes, improve efficiencies and sharpen profit visibility with Velmarin's advanced metrics, flexible functionality and user-friendly interface.</p>
  <div class="btn" style="left:237px;top:377px;width:140px;height:30px">Demo</div>
  <div class="video" role="img" aria-label="Video still of an animated presenter at a lectern with a time and money thought bubble"><div class="play"></div></div>
  <p class="caption">Integrating project and resource management with billing.</p>
</section>

<section class="partner">
  <div class="rule"></div>
  <h2 class="headline">partner with<br>cloudmerit</h2>
  <p class="lead">Implement procedures, methodologies and compliance with ease.</p>
  <p class="note">Just create checklists to ensure consistency.</p>
  <p class="copy">You can add checklists manually to any objects, creating Cloudmerit Tasks. Checklists can be general or for specific Cloudmerit or Custom objects (e.g. Accounts, Opportunities) - and can be restricted to certain criteria, e.g. Accounts with a Rating of Warm.</p>
  <ul class="checks">
    <li><svg width="18" height="18" viewBox="0 0 18 18" fill="none" stroke="#7dc33b" stroke-width="2"><rect x="1" y="1" width="16" height="16"/><path d="M4 9l4 4 8-10"/></svg>Tasknote7qx works for everyone</li>
    <li><svg width="18" height="18" viewBox="0 0 18 18" fill="none" stroke="#7dc33b" stroke-width="2"><rect x="1" y="1" width="16" height="16"/><path d="M4 9l4 4 8-10"/></svg>Harbor or Classic UI</li>
    <li><svg width="18" height="18" viewBox="0 0 18 18" fill="none" stroke="#7dc33b" stroke-width="2"><rect x="1" y="1" width="16" height="16"/><path d="M4 9l4 4 8-10"/></svg>any Cloudmerit Edition</li>
  </ul>
  <div class="badge"><span></span></div>
  <div class="panel">
    <div class="bar"></div>
    <h4>Open Task Summary</h4>
    <svg width="377" height="90" viewBox="0 0 377 90">
      <g transform="translate(48,42)"><circle r="34" fill="#7dc33b"/><path d="M0 0L0 -34A34 34 0 0 1 30 16Z" fill="#2b7bd6"/></g>
      <g transform="translate(140,42)"><circle r="34" fill="#7dc33b"/><path d="M0 0L0 -34A34 34 0 0 1 34 0Z" fill="#2b7bd6"/></g>
      <g transform="translate(232,42)"><circle r="34" fill="#2b7bd6"/><path d="M0 0L0 -34A34 34 0 0 0 -34 0Z" fill="#7dc33b"/><path d="M0 0L-34 0A34 34 0 0 0 0 34Z" fill="#e07b24"/></g>
      <g transform="translate(324,42)"><circle r="34" fill="#7dc33b"/><path d="M0 0L-34 0A34 34 0 0 0 20 28Z" fill="#e07b24"/><path d="M0 0L34 0A34 34 0 0 0 0 -34Z" fill="#2b7bd6"/></g>
    </svg>
    <h4>Related To Tasks</h4>
    <table>
      <tr><th>Object</th><th>Related To</th><th>Open</th><th>Closed</th><th>Status</th></tr>
      <tr><td>Account</td><td>Alder Co</td><td>2</td><td>0</td><td>Not Started</td></tr>
      <tr><td>Opportunity</td><td>Renewal Q4</td><td>1</td><td>2</td><td>In Progress</td></tr>
      <tr><td>Opportunity</td><td>New Seats</td><td>3</td><td>1</td><td>Completed</td></tr>
    </table>
    <h4>Open Task Details</h4>
    <table>
      <tr><th>Object</th><th>Related To</th><th>Subject</th><th>Due</th></tr>
      <tr><td>Account</td><td>Alder Co</td><td>Call to confirm scope</td><td>07/16</td></tr>
      <tr><td>Opportunity</td><td>Renewal Q4</td><td>Send proposal draft</td><td>07/18</td></tr>
    </table>
  </div>
</section>

<section class="demo">
  <div class="rule dark"></div>
  <h2 class="headline">see time+expenses demo work in your organization</h2>
  <p class="sub">Lorem Ipsum is simply dummy text of the printing and typesetting industry.</p>
  <div class="btn" style="left:237px;top:310px;width:172px;height:30px">Schedule a demo</div>
  <div class="portrait" role="img" aria-label="Photo of a smiling businessman in a grey suit with arms crossed"></div>
</section>

<section class="news">
  <h2>LATEST NEWS</h2>
  <article class="card" style="left:160px">
    <div class="date"><div class="d">19</div><div class="m">SEP</div></div>
    <h3>Enter Time – Mobile</h3>
    <p class="meta">Posted by: Lenn Ostrava &nbsp;&nbsp; Comments: 0 comments</p>
    <p class="excerpt">If you are on the go, you can capture time also from any mobile device or browser.<br>&nbsp;› &nbsp;in the Welcome Tab, click on Mobile or go directly to… <a class="more">READ MORE</a></p>
  </article>
  <article class="card" style="left:610px">
    <div class="date"><div class="d">20</div><div class="m">AUG</div></div>
    <h3>Enter Time – Mobile</h3>
    <p class="meta">Posted by: Lenn Ostrava &nbsp;&nbsp; Comments: 0 comments</p>
    <p class="excerpt">If you are on the go, you can capture time also from any mobile device or browser.<br>&nbsp;› &nbsp;in the Welcome Tab, click on Mobile or go directly to… <a class="more">READ MORE</a></p>
  </article>
  <div class="btn" style="left:532px;top:315px;width:136px;height:30px">See all</div>
</section>

<section class="newsletter">
  <h2>Subscribe to Our Newsletter</h2>
  <div class="field">Enter Email</div>
  <div class="btn">Subscribe</div>
</section>

<footer class="site-footer">
  <div class="brand"><span class="dot"></span>Velmarin</div>
  <p class="about">Lorem Ipsum is simply dummy text of the printing and typesetting industry. Lorem Ipsum has been the industry's standard dummy text ever since the 1500s, when an unknown printer took a galley of type and scrambled it to make a type specimen book.</p>
  <p class="copyright">Copyright © Velmarin, 1999-2019</p>
  <div class="fcol" style="left:463px">
    <h4>SITEMAP</h4>
    <ul><li>Home</li><li>Featured Products</li><li>Solutions</li><li>Support</li><li>Blog</li></ul>
  </div>
  <div class="fcol" style="left:655px">
    <h4>QUICK LINKS</h4>
    <ul><li>Demo</li><li>Support</li><li>Documentation</li><li>Privacy</li><li>Terms</li><li>Contact</li></ul>
  </div>
  <div class="fcol contact" style="left:837px">
    <h4>CONTACT US</h4>
    <ul>
      <li style="height:36px"><svg width="10" height="13" viewBox="0 0 10 13"><path d="M5 0a5 5 0 0 0-5 5c0 4 5 8 5 8s5-4 5-8a5 5 0 0 0-5-5z" fill="#fff"/><circle cx="5" cy="5" r="2" fill="#5ea4b4"/></svg><span>18 Alder Court # 210 Brookvale,<br>CA 90417</span></li>
      <li><svg width="11" height="11" viewBox="0 0 11 11"><path d="M2 0l2 3-1 1c1 2 2 3 4 4l1-1 3 2-1 2C5 11 0 6 0 2z" fill="#fff"/></svg>+1 (555) 014-2290</li>
      <li><svg width="12" height="9" viewBox="0 0 12 9"><rect width="12" height="9" fill="#fff"/><path d="M0 0l6 5 6-5" stroke="#5ea4b4" fill="none"/></svg>info@velmarin.com</li>
    </ul>
    <div class="social"><span></span><span></span><span></span><span></span></div>
  </div>
</footer>

</body>
</html>
```